Campaign Flyer for a local election

Black and white election flyer

See information below to be included:

Re-elect Dorian
Experienced Willows Board Member
Experienced NYC Principal
Experienced leader

One Year Board Accomplishments:
-Installed New Park Lights (Bollards)
-Red Brick Road Repair Project
-Established Closer Ties with Our local precinct to frequently monitor the community with directed security patrols. Requested an increased police presence.
-Met with the 62nd Precinct Officials & Assemblywoman, Marla Quintrell to discuss our security issues
- Focused on maintenance of streetlights to make brighter streets
-Negotiated Contract & Hired Our New Landscaper, Oakhollow Landscapers
-Major Homeowner Shrub Replacement Project
- Addressing Standing Water in our Park (Installed French Drain)
- Replaced and upgraded all 5 outdoor circuit breaker panels
-Write monthly community newsletters
-Sewer cleaning project (had all community catch basins cleaned)
-Carefully overseeing our new school project. Coordinating with the sponsor and the school directors
-Delivered a very healthy budget to the community
-Works closely with our committees
-Events: Zoo event, Petting Zoo, Outdoor Movie Night, Egg Hunt

It is my intent to seek re-election.
(Photo) Dorian Lindqvist
-Dedicated to improving our community
-Hard-working…He gets thing done!
-Trustworthy

. .

Please note, I am submitting new information under accomplishments. The list of accomplishments should be in the same sequence, starting with: Met with the 62nd Precinct....
Please carefully review.
----------------------------------------------------------------------------------------------------------------------------------------------------------------

Re-elect Dorian
Experienced NYC Principal
Experienced leader

Last Year’s Board Accomplishments:

-Met with the 62nd Precinct Officials & Assemblywoman, Marla Quintrell, to discuss our security issues. Requested increased police presence.
-Established a strong partnership with the 62nd precinct to frequently monitor the community with directed security patrols.
-Replaced all new park lights (Bollards) to make the park brighter
- Focused on maintenance of streetlights to make streets brighter
-‘Fixing Our Streets Project’ (Repaired all cracked/missing red bricks)
-Homeowner Shrub Replacement Project (Replaced hundreds of bushes)
- I write the monthly community newsletter
-Carefully overseeing our new school project. Coordinating with the sponsor and the school director
-Monitoring C of O’s and homeowners Insurance

(Photo) Dorian Lindqvist
-Hard-working! I get things done!
-Trustworthy

. .

Re-elect Dorian
Experienced NYC Principal
Experienced leader

(Photo) Dorian Lindqvist
-Trustworthy

. .

Target Market(s)

A Community electing a Board Member

Industry/Entity Type

residential election

Requirements
Must have
• all black, white and grey print. Flyers will not be printed in color
Nice to have
• See the information in the attachment below containing all my accomplishments
Should not have
• color

```html
<!DOCTYPE html>
<html lang="en">
<head>
<meta charset="utf-8">
<title>Re-elect Dorian – Campaign Flyer</title>
<link rel="stylesheet" href="https://fonts.googleapis.com/css2?family=Anton&family=Roboto+Condensed:ital,wght@0,400;0,700;1,700&display=swap">
<style>
  :root {
    --black: #000000;
    --white: #ffffff;
    --ink: #1a1a1a;
    --grey-dark: #3c3c3c;
    --grey-mid: #7a7a7a;
    --grey-light: #c8c8c8;
    --rule: #9a9a9a;
  }
  * { margin: 0; padding: 0; box-sizing: border-box; }
  html, body { width: 1200px; height: 1095px; overflow: hidden; background: var(--white); }
  body { position: relative; font-family: "Roboto Condensed", sans-serif; }

  .flyer { position: absolute; left: 279px; top: 106px; width: 651px; height: 920px; background: var(--black); overflow: hidden; }

  .beach-scene { position: absolute; left: 0; top: 0; width: 651px; height: 458px;
    background: linear-gradient(180deg, #0a0a0a 0%, #4a4a4a 14%, #9a9a9a 26%, #6e6e6e 40%, #8a8a8a 60%, #5a5a5a 100%); }

  .candidate-photo { position: absolute; left: 414px; top: 212px; width: 237px; height: 560px;
    background: radial-gradient(ellipse at 50% 25%, #bdbdbd 0%, #8a8a8a 30%, #2a2a2a 60%, #000 90%); }

  .headline { position: absolute; left: 34px; top: 30px; font-family: "Anton", sans-serif;
    font-size: 98px; line-height: 1.1; letter-spacing: -1px; white-space: nowrap; }
  .headline .verb { color: var(--white); -webkit-text-stroke: 3px var(--black); paint-order: stroke fill; }
  .headline .first-name { color: var(--black); -webkit-text-stroke: 3px var(--white); paint-order: stroke fill; }

  .credentials { position: absolute; left: 44px; top: 146px; list-style: none; }
  .credentials li { display: flex; align-items: center; height: 36px; color: var(--white);
    font-weight: 700; font-size: 29px; text-shadow: 0 1px 3px rgba(0,0,0,.6); }
  .credentials svg { width: 24px; height: 24px; margin-right: 10px; }

  .accomplishments-title { position: absolute; left: 45px; top: 263px; width: 366px; height: 60px;
    background: linear-gradient(90deg, var(--black) 60%, #3a3a3a 100%);
    color: var(--white); font-weight: 700; font-size: 21px; line-height: 24px; padding: 8px 0 0 14px; }

  .accomplishments { position: absolute; left: 45px; top: 323px; width: 356px; background: var(--white);
    padding-bottom: 28px;
    clip-path: polygon(0 0, 100% 0, 100% calc(100% - 28px), 52% 100%, 0 calc(100% - 28px)); }
  .accomplishments ul { list-style: none; padding: 3px 20px 0 13px; }
  .accomplishments li { position: relative; padding: 3px 0 3px 10px; font-size: 10.4px; line-height: 12.5px;
    color: var(--ink); border-bottom: 1px solid var(--rule); }
  .accomplishments li:last-child { border-bottom: none; }
  .accomplishments li::before { content: ""; position: absolute; left: -3px; top: 6px; width: 6px; height: 6px;
    border-radius: 50%; background: var(--ink); }

  .vote-badge { position: absolute; left: 325px; top: 228px; width: 92px; height: 92px; }

  .pledge { position: absolute; left: 0; width: 651px; top: 728px; text-align: center; color: var(--white);
    font-style: italic; font-weight: 700; font-size: 21px; }

  .candidate-name { position: absolute; left: 0; width: 651px; top: 748px; text-align: center;
    font-family: "Anton", sans-serif; font-size: 80px; line-height: 1.15; letter-spacing: -0.5px;
    background: linear-gradient(180deg, #ffffff 20%, #bcbcbc 70%, #8c8c8c 100%);
    -webkit-background-clip: text; background-clip: text; color: transparent; }

  .tagline-band { position: absolute; left: 0; top: 846px; width: 651px; height: 74px; text-align: center;
    background: linear-gradient(90deg, #a8a8a8 0%, #f2f2f2 50%, #a8a8a8 100%); padding-top: 9px; }
  .tagline-band .mission { color: var(--grey-mid); font-weight: 700; font-size: 18.5px; line-height: 24px; }
  .tagline-band .qualities { color: var(--black); font-weight: 700; font-size: 18.5px; line-height: 24px; }
</style>
</head>
<body>
<main class="flyer">
  <div class="beach-scene" role="img" aria-label="Black and white photo of a beach with dune grass and a fence along the shoreline"></div>
  <div class="candidate-photo" role="img" aria-label="Portrait photo of candidate Dorian Lindqvist in suit and tie"></div>

  <h1 class="headline"><span class="verb">Re-elect</span> <span class="first-name">Dorian</span></h1>

  <ul class="credentials">
    <li><svg viewBox="0 0 24 24"><path d="M3 13l6 6L21 5" fill="none" stroke="#fff" stroke-width="3.2"/></svg>Experienced Willows Board Member</li>
    <li><svg viewBox="0 0 24 24"><path d="M3 13l6 6L21 5" fill="none" stroke="#fff" stroke-width="3.2"/></svg>Experienced NYC Principal</li>
    <li><svg viewBox="0 0 24 24"><path d="M3 13l6 6L21 5" fill="none" stroke="#fff" stroke-width="3.2"/></svg>Experienced Leader</li>
  </ul>

  <h2 class="accomplishments-title">Last Year’s<br>Board Accomplishments:</h2>

  <section class="accomplishments">
    <ul>
      <li>Met with the 62nd Precinct Officials &amp; Assemblywoman, Marla Quintrell, to discuss our security issues. Requested increased police presence.</li>
      <li>Established a strong partnership with the 62nd precinct to frequently monitor the community with directed security patrols.</li>
      <li>Replaced all new park lights (Bollards) to make the park brighter</li>
      <li>Focused on maintenance of streetlights to make streets brighter</li>
      <li>‘Fixing Our Streets Project’ (Repaired all cracked/missing red bricks)</li>
      <li>Negotiated Contract &amp; Hired Our New Landscaper, Oakhollow Landscapers</li>
      <li>Homeowner Shrub Replacement Project (Replaced hundreds of bushes)</li>
      <li>Addressing Standing Water in our Park (Installed French Drain)</li>
      <li>Replaced and upgraded all 5 outdoor circuit breaker panels</li>
      <li>I write the monthly community newsletter</li>
      <li>Sewer cleaning project (had all community catch basins cleaned)</li>
      <li>Carefully overseeing our new school project. Coordinating with the sponsor and the school director</li>
      <li>Delivered a very healthy budget to the community with over $1,000,000 in operating funds and reserves</li>
      <li>Works closely with our committees</li>
      <li>Monitoring C of O’s and homeowners Insurance</li>
      <li>Events: Petting Zoo, Outdoor Movie Night, Egg Hunt</li>
    </ul>
  </section>

  <svg class="vote-badge" viewBox="0 0 92 92">
    <defs>
      <radialGradient id="badgeShade" cx="40%" cy="35%" r="70%">
        <stop offset="0%" stop-color="#ffffff"/><stop offset="100%" stop-color="#bdbdbd"/>
      </radialGradient>
      <path id="badgeRing" d="M46,46 m-32,0 a32,32 0 1,1 64,0 a32,32 0 1,1 -64,0"/>
    </defs>
    <circle cx="46" cy="46" r="45" fill="url(#badgeShade)"/>
    <text font-family="Roboto Condensed, sans-serif" font-weight="700" font-size="10.5" fill="#111" letter-spacing="1.2">
      <textPath href="#badgeRing">VOTE · VOTE · VOTE · VOTE · VOTE ·</textPath>
    </text>
    <path d="M33 46l9 9 17-19" fill="none" stroke="#111" stroke-width="5"/>
  </svg>

  <p class="pledge">"It is my intent to seek re-election"</p>
  <p class="candidate-name">Dorian Lindqvist</p>

  <footer class="tagline-band">
    <p class="mission">Dedicated to improving our community</p>
    <p class="qualities">Hard-working! He gets things done! Trustworthy!</p>
  </footer>
</main>
</body>
</html>
```